Designing a Business Card

Hello!

I have started a digital advertising agency, and I'm looking for a design concept for my business card.

The company name is Brindle Metrics. and the info below should appear on the card (feel free to change the layout or structure):

Name: Owen Tarrant
Title: Founder
Address: 412-448 Larkspur Blvd., Winnipeg, MB R2K 4W8, Canada
Office: +1 (833) 555-0172 | +1 (431) 555-0172
Cell: +1 (431) 555-0179
Email: Owen@[login to view URL]
Website: [login to view URL]
Logo: [login to view URL]

The business card size will be 3.5 x 2, double-sided color printing.

I'm looking for a design that will integrate the style of the logo into the entire card theme, so any entry that was made directly from a template will be eliminated from consideration.

```html
<!DOCTYPE html>
<html lang="en">
<head>
<meta charset="utf-8">
<title>Brindle Metrics – Business Card</title>
<link rel="stylesheet" href="https://fonts.googleapis.com/css2?family=Arimo:wght@400;700&family=Tinos:wght@400&display=swap">
<style>
  :root {
    --backdrop: #1a1a1a;
    --card: #262626;
    --ink: #f2f2f2;
    --muted: #8c8c8c;
    --blue: #4a7fd4;
    --red: #e8413a;
    --green: #2fb24c;
    --yellow: #f5b400;
    --globe: #9a9a9a;
  }
  * { box-sizing: border-box; margin: 0; padding: 0; }
  html, body { width: 1200px; height: 900px; overflow: hidden; }
  body {
    background: var(--backdrop);
    font-family: "Arimo", Arial, sans-serif;
    color: var(--ink);
    position: relative;
  }
  .card {
    position: absolute;
    left: 250px;
    width: 700px;
    height: 400px;
    background: var(--card);
  }
  .card--front { top: 35px; }
  .card--back { top: 465px; }

  /* Front */
  .brand-block {
    position: absolute;
    left: 50px;
    top: 140px;
    width: 280px;
    text-align: center;
  }
  .wordmark {
    font-family: "Arimo", Arial, sans-serif;
    font-weight: 700;
    color: var(--muted);
    white-space: nowrap;
  }
  .brand-block .wordmark { font-size: 30px; }
  .address {
    margin-top: 28px;
    font-family: "Tinos", "Times New Roman", serif;
    font-size: 16px;
    line-height: 1.35;
    color: var(--ink);
  }
  .address svg { display: block; margin: 0 auto 6px; }

  .contact-block {
    position: absolute;
    left: 395px;
    top: 70px;
    width: 270px;
  }
  .person-name {
    font-size: 24px;
    font-weight: 400;
    line-height: 1.1;
  }
  .person-name .first { color: var(--blue); }
  .person-name .last { color: var(--red); }
  .person-title {
    font-size: 16px;
    color: var(--green);
    padding-bottom: 4px;
    border-bottom: 2px solid var(--yellow);
    width: 190px;
  }
  .contact-list { list-style: none; margin-top: 18px; }
  .contact-list li {
    display: flex;
    align-items: center;
    gap: 6px;
    font-size: 18px;
    line-height: 28px;
    white-space: nowrap;
  }
  .contact-list svg { flex: none; }

  /* Back */
  .card--back .wordmark {
    position: absolute;
    left: 0; right: 0;
    top: 140px;
    text-align: center;
    font-size: 56px;
  }
  .site-line {
    position: absolute;
    left: 0; right: 0;
    bottom: 48px;
    display: flex;
    justify-content: center;
    align-items: center;
    gap: 8px;
    font-size: 22px;
    color: var(--blue);
  }
</style>
</head>
<body>

<section class="card card--front">
  <div class="brand-block">
    <div class="wordmark">Brindle Metrics</div>
    <p class="address">
      <svg width="16" height="22" viewBox="0 0 16 22" aria-hidden="true"><path d="M8 0a8 8 0 0 0-8 8c0 6 8 14 8 14s8-8 8-14a8 8 0 0 0-8-8z" fill="#e8413a"/><circle cx="8" cy="8" r="3" fill="#262626"/></svg>
      412-448 Larkspur Blvd.,<br>Winnipeg, MB R2K 4W8, Canada
    </p>
  </div>

  <div class="contact-block">
    <div class="person-name"><span class="first">Owen</span> <span class="last">Tarrant</span></div>
    <div class="person-title">Founder</div>
    <ul class="contact-list">
      <li>
        <svg width="20" height="20" viewBox="0 0 20 20" aria-hidden="true"><circle cx="10" cy="10" r="10" fill="#2fb24c"/><path d="M6 5.5l2 0 1 3-1.3 1a6 6 0 0 0 3 3l1-1.3 3 1v2a1.5 1.5 0 0 1-1.6 1.3A9 9 0 0 1 4.7 7 1.5 1.5 0 0 1 6 5.5z" fill="#fff"/></svg>
        +1 (431) 555-0179
      </li>
      <li>
        <svg width="20" height="20" viewBox="0 0 20 20" aria-hidden="true"><circle cx="10" cy="10" r="10" fill="#e8413a"/><path d="M4 8c0-2 12-2 12 0v1.5h-3V8H7v1.5H4z" fill="#fff"/><rect x="6" y="10" width="8" height="4.5" rx="1" fill="#fff"/></svg>
        +1 (833) 555-0172
      </li>
      <li>
        <svg width="20" height="20" viewBox="0 0 20 20" aria-hidden="true"><circle cx="10" cy="10" r="10" fill="#e8413a"/><path d="M4 8c0-2 12-2 12 0v1.5h-3V8H7v1.5H4z" fill="#fff"/><rect x="6" y="10" width="8" height="4.5" rx="1" fill="#fff"/></svg>
        +1 (431) 555-0172
      </li>
      <li>
        <svg width="20" height="20" viewBox="0 0 20 20" aria-hidden="true"><circle cx="10" cy="10" r="10" fill="#4a7fd4"/><rect x="5" y="6.5" width="10" height="7" rx="1" fill="#fff"/><path d="M5.5 7l4.5 3.5L14.5 7" stroke="#4a7fd4" stroke-width="1.2" fill="none"/></svg>
        Owen@brindle-metrics.com
      </li>
      <li>
        <svg width="20" height="20" viewBox="0 0 20 20" aria-hidden="true"><g fill="none" stroke="#9a9a9a" stroke-width="1.4"><circle cx="10" cy="10" r="8.5"/><ellipse cx="10" cy="10" rx="3.6" ry="8.5"/><path d="M1.5 10h17M3 5.5h14M3 14.5h14"/></g></svg>
        www.brindle-metrics.com
      </li>
    </ul>
  </div>
</section>

<section class="card card--back">
  <div class="wordmark">Brindle Metrics</div>
  <div class="site-line">
    <svg width="22" height="22" viewBox="0 0 20 20" aria-hidden="true"><g fill="none" stroke="#9a9a9a" stroke-width="1.4"><circle cx="10" cy="10" r="8.5"/><ellipse cx="10" cy="10" rx="3.6" ry="8.5"/><path d="M1.5 10h17M3 5.5h14M3 14.5h14"/></g></svg>
    brindle-metrics.com
  </div>
</section>

</body>
</html>
```